Business card for a shipping supplies business

Needing a business card design. Please see the logo. The logo with the white font should be used if there is a dark background.

We are looking for the following info on the card. Please see the sample info. We will need the info to be changed with a few different employee names and info but all will use the same template.

Business Name: The Crate Heron
Employee Name : Marcus Delaney
Position: Account Manager
Address: 4827 W. Ridge 418 S.
Fort Worth, TX 73948
email: Marcus@thecrateheron.example
telephone: 855-619-2740 x 207
website: www.getparcelkits.example

Target Market(s)

Businesses who ship products for online sales

Industry/Entity Type

Cardboard

Contact Information for Business Card

Name, title, address, website, logo, telephone number

Font styles to use
Sans Serif

Colors
EE7325
F08F49
F5BC92
FAE3D3
FDF4ED

Requirements
Must have
• Logo on back of card. Clean look, just logo, website address

```html
<!DOCTYPE html>
<html lang="en">
<head>
<meta charset="utf-8">
<title>The Crate Heron – Business Card</title>
<link rel="stylesheet" href="https://fonts.googleapis.com/css2?family=Poppins:wght@400;500;600;700&display=swap">
<style>
  :root {
    --page: #f5e5da;
    --kraft: #bd8b69;
    --cocoa: #3e302c;
    --ink: #1a1513;
    --rust: #d0532a;
    --white: #ffffff;
  }
  * { box-sizing: border-box; margin: 0; padding: 0; }
  html, body { width: 1200px; height: 800px; overflow: hidden; }
  body { background: var(--page); font-family: "Poppins", sans-serif; position: relative; }

  .card { position: absolute; top: 261px; width: 488px; height: 279px; border-radius: 26px; overflow: hidden; }

  /* Back of card */
  .card-back { left: 87px; background: var(--kraft); }
  .card-back .band { position: absolute; left: 0; right: 0; top: 77px; height: 126px; background: var(--cocoa); }
  .card-back .rule { position: absolute; top: 62px; height: 2px; background: var(--rust); }
  .card-back .rule.left { left: 0; width: 155px; }
  .card-back .rule.right { left: 333px; right: 0; }
  .card-back .brand { position: absolute; left: 0; right: 0; top: 84px; text-align: center;
    color: var(--white); font-weight: 600; font-size: 22px; letter-spacing: 0.5px; line-height: 36px; white-space: nowrap; }
  .card-back .web { position: absolute; left: 0; right: 0; top: 248px; display: flex; justify-content: center;
    align-items: center; gap: 7px; color: var(--cocoa); font-size: 12px; font-weight: 500; }
  .card-back .web svg { width: 12px; height: 12px; }

  /* Front of card */
  .card-front { left: 625px; background: var(--white); }
  .card-front .head { position: absolute; left: 0; right: 0; top: 0; height: 84px; background: var(--cocoa); }
  .card-front .name { position: absolute; left: 22px; top: 20px; color: var(--white); font-weight: 700; font-size: 22px; line-height: 28px; letter-spacing: -0.2px; white-space: nowrap; }
  .card-front .role { position: absolute; left: 22px; top: 47px; color: var(--white); font-size: 13px; font-weight: 500; letter-spacing: 0.4px; }
  .card-front .address-band { position: absolute; left: 0; right: 0; top: 84px; height: 62px; background: var(--kraft); }
  .contact { position: absolute; left: 18px; display: flex; align-items: center; gap: 11px; font-size: 12px; white-space: nowrap; }
  .contact .icon { width: 24px; height: 24px; border-radius: 50%; background: var(--rust); display: flex;
    align-items: center; justify-content: center; flex: none; }
  .contact .icon svg { width: 13px; height: 13px; }
  .contact.address { top: 102px; color: var(--white); line-height: 14px; }
  .contact.email { top: 167px; color: var(--rust); }
  .contact.phone { top: 198px; color: var(--rust); }
  .contact.site { top: 230px; color: var(--rust); }
  .card-front .brand { position: absolute; right: 26px; bottom: 22px; display: flex; align-items: center; gap: 8px;
    color: var(--ink); font-weight: 600; font-size: 18px; white-space: nowrap; }
  .card-front .brand .dot { width: 14px; height: 14px; border-radius: 50%; background: var(--rust); }
</style>
</head>
<body>

<section class="card card-back" aria-label="Back of business card">
  <div class="band">
    <div class="rule left"></div>
    <div class="rule right"></div>
    <div class="brand">The Crate Heron</div>
  </div>
  <div class="web">
    <svg viewBox="0 0 12 12" fill="none" stroke="#3e302c" stroke-width="1"><circle cx="6" cy="6" r="5"/><path d="M1 6h10M6 1c2 2 2 8 0 10M6 1c-2 2-2 8 0 10"/></svg>
    <span>www.getparcelkits.example</span>
  </div>
</section>

<section class="card card-front" aria-label="Front of business card">
  <div class="head">
    <h1 class="name">MARCUS DELANEY</h1>
    <p class="role">Account&nbsp; Manager</p>
  </div>
  <div class="address-band"></div>

  <div class="contact address">
    <span class="icon"><svg viewBox="0 0 14 14" fill="#fff"><path d="M7 1 1 6.5h2V13h3V9h2v4h3V6.5h2z"/></svg></span>
    <span>4827 W. Ridge 418 S.<br>Fort Worth, TX 73948</span>
  </div>
  <div class="contact email">
    <span class="icon"><svg viewBox="0 0 14 14" fill="#fff"><path d="M1 2l12 5-12 5 2.5-5z"/></svg></span>
    <span>Marcus@thecrateheron.example</span>
  </div>
  <div class="contact phone">
    <span class="icon"><svg viewBox="0 0 14 14" fill="#fff"><path d="M1 5c0-2 12-2 12 0v1.5h-3V5H4v1.5H1z"/><path d="M3 7h8l1 5H2z"/><circle cx="7" cy="9.5" r="1.3" fill="#d0532a"/></svg></span>
    <span>855-619-2740 x 207</span>
  </div>
  <div class="contact site">
    <span class="icon"><svg viewBox="0 0 14 14" fill="none" stroke="#fff" stroke-width="1.2"><circle cx="7" cy="7" r="5.5"/><path d="M1.5 7h11M7 1.5c2.5 2.5 2.5 8.5 0 11M7 1.5c-2.5 2.5-2.5 8.5 0 11"/></svg></span>
    <span>www.getparcelkits.example</span>
  </div>

  <div class="brand"><span class="dot"></span><span>The Crate Heron</span></div>
</section>

</body>
</html>
```